Letterhead for New Orthopaedic Surgery Practice

My husband and I are starting our own practice named RB Spine & Vitality Center. We would like to create a nice simple but high class letterhead that doesn't use too much solid color ink when printing. I like the colors dark blue, gold, yellow. Open to other suggestions. We will need to list him and I both on the top of the letterhead. Here is the important information:
Lucinda Perrow, M.D. - Hand and Upper Extremity Surgery
Abena Quist, M.D. - Hip & Knee Replacement/General Orthopaedic Surgery
Location: 18735 North Harlow Pkwy
Palm Crest, FL 33482
Phone: 954-218-4650
Fax: 954-582-1346
Email: info@myrbspine.com

The only thing is that the phone and fax numbers will change once we get into our space. I just want to get the design started. I am including several documents which are my previous practice letterhead, my current procedure room letterhead, and our new Logo. The other letterheads are just for examples but please think outside of the box! We would love to see some great designs.

Colors
0054AA
0677BA
7BADD7
CADEEF
E8F1F8
0094D4
00A9DD
6FCCEA
C7EBF8
E9F6FB

Requirements
Must have
• class, elegance, luxury

```html
<!DOCTYPE html>
<html lang="en">
<head>
<meta charset="utf-8">
<title>RB Spine &amp; Vitality Center Letterhead</title>
<link rel="stylesheet" href="https://fonts.googleapis.com/css2?family=Montserrat:wght@400;500;600&family=Source+Sans+3:wght@400&display=swap">
<style>
  :root {
    --navy: #1b2a52;
    --gold: #c4a060;
    --ink: #2b2b2b;
    --muted: #5f5f5f;
    --paper: #ffffff;
    --backdrop: #dedede;
  }
  * { box-sizing: border-box; margin: 0; padding: 0; }
  html, body { width: 1153px; height: 1200px; overflow: hidden; background: var(--backdrop); }
  .sheet {
    position: absolute; left: 128px; top: 20px;
    width: 896px; height: 1160px;
    background: var(--paper);
    font-family: "Montserrat", sans-serif;
    color: var(--ink);
    overflow: hidden;
  }
  .brand {
    position: absolute; left: 69px; top: 50px; width: 204px; height: 204px;
    border: 2px solid var(--gold); border-radius: 50%;
    display: flex; align-items: center; justify-content: center; text-align: center;
    color: var(--navy); font-weight: 600; font-size: 19px; line-height: 1.3;
  }
  .practice-info {
    position: absolute; right: 72px; top: 37px; text-align: right;
    font-size: 16px; line-height: 21px; color: var(--ink);
  }
  .practice-info .row { display: flex; justify-content: flex-end; align-items: center; gap: 6px; }
  .practice-info .row svg { width: 12px; height: 12px; fill: var(--navy); flex: none; }
  .practice-info .group { margin-bottom: 8px; }
  .practice-info .doctor { margin-top: 17px; }
  .practice-info .doctor + .doctor { margin-top: 15px; }
  .rule { position: absolute; left: 135px; top: 349px; width: 2px; height: 740px; background: var(--navy); }
  .sender { position: absolute; left: 193px; top: 341px; }
  .sender .name { font-weight: 600; font-size: 18px; line-height: 20px; }
  .sender .title { font-size: 16px; line-height: 19px; }
  .sender dl { margin-top: 16px; display: grid; grid-template-columns: 27px auto; row-gap: 4px; font-size: 16px; line-height: 18px; align-items: baseline; }
  .sender dt { font-weight: 600; font-size: 15px; }
  .letter-body {
    position: absolute; left: 191px; top: 540px; width: 639px;
    font-family: "Source Sans 3", sans-serif; font-size: 16px; line-height: 31px;
    text-align: justify; color: var(--ink);
  }
  .letter-body p + p { margin-top: 31px; }
  .signature { position: absolute; left: 188px; top: 988px; width: 212px; height: 40px;
    background: linear-gradient(90deg, #ececec, #f6f6f6); border-radius: 4px; }
  .signer { position: absolute; left: 188px; top: 1033px; color: var(--muted); }
  .signer .name { font-size: 23px; font-weight: 500; line-height: 28px; }
  .signer .title { font-size: 17px; line-height: 24px; }
  .footer-band {
    position: absolute; left: 0; bottom: 0; width: 896px; height: 26px;
    background: linear-gradient(90deg, var(--gold), var(--navy) 50%, var(--gold));
  }
</style>
</head>
<body>
  <div class="sheet">
    <div class="brand">RB Spine &amp;<br>Vitality<br>Center</div>

    <div class="practice-info">
      <div class="group">
        <div class="row"><span>18735 North Harlow Pkwy</span>
          <svg viewBox="0 0 12 12"><path d="M6 0a4 4 0 0 0-4 4c0 3 4 8 4 8s4-5 4-8a4 4 0 0 0-4-4zm0 5.5A1.5 1.5 0 1 1 6 2.5a1.5 1.5 0 0 1 0 3z"/></svg></div>
        <div class="row"><span>Palm Crest, FL 33482</span><span style="width:12px"></span></div>
      </div>
      <div class="row"><span>954-218-4650</span>
        <svg viewBox="0 0 12 12"><path d="M1 4c0-2 2-3 5-3s5 1 5 3v1H8V4H4v1H1zM3 6h6l2 5H1z"/></svg></div>
      <div class="row"><span>954-582-1346</span>
        <svg viewBox="0 0 12 12"><path d="M3 1h6v3H3zM1 5h10v5H9V8H3v2H1zM4 9h4v2H4z"/></svg></div>
      <div class="row"><span>info@myrbspine.com</span>
        <svg viewBox="0 0 12 12"><path d="M1 3h10v7H1zM1.5 3.5 6 7l4.5-3.5" fill="var(--navy)" stroke="#fff" stroke-width=".8"/></svg></div>
      <div class="doctor">Lucinda Perrow, M.D.<br>Hand and Upper Extremity Surgery</div>
      <div class="doctor">Abena Quist, M.D.<br>Hip &amp; Knee Replacement General Orthopaedic Surgery</div>
    </div>

    <div class="rule"></div>

    <div class="sender">
      <div class="name">Your Name</div>
      <div class="title">Managing Director</div>
      <dl>
        <dt>A</dt><dd>123 Your address here</dd>
        <dt>P</dt><dd>123-456-789</dd>
        <dt>E</dt><dd>www.yourwebsite.com</dd>
        <dt>W</dt><dd>info@yourmail.com</dd>
      </dl>
    </div>

    <div class="letter-body">
      <p>Lorem Ipsum es simplemente el texto de relleno de las imprentas y archivos de texto. Lorem Ipsum ha sido el texto de relleno estándar de las industrias desde el año 1500, cuando un impresor (N. del T. persona que se dedica a la imprenta) desconocido usó</p>
      <p>un libro de textos especimen. No sólo sobrevivió 500 años, sino que tambien ingresó como texto de relleno en documentos electrónicos, quedando esencialmente igual al original. Fue popularizado en los 60s con la creación de las hojas "Lettrafix", las cuales contenian pasajes de Lorem Ipsum, y más recientemente con software de autoedición, como por ejemplo Verso PageForm, el cual incluye versiones de Lorem Ipsum.</p>
      <p>"Lorem Ipsum" va a dar por resultado muchos sitios web que usan este texto si se encuentran en estado de desarrollo. Muchas versiones han evolucionado a través de los años, algunas veces por accidente, otras veces a propósito (por ejemplo insertándole humor y cosas por el estilo).</p>
    </div>

    <div class="signature" role="img" aria-label="Handwritten signature of Dorian Kessler"></div>
    <div class="signer">
      <div class="name">Dorian Kessler</div>
      <div class="title">Managing Director</div>
    </div>

    <div class="footer-band" role="img" aria-label="Decorative gold and navy footer band"></div>
  </div>
</body>
</html>
```